Albeto Wine Label For Harbor Grove

Cedar Bend Winery is in need of a wine label for new wine being release. This wine will be used as a fundraiser for Harbor Grove, a chimpanzee santuary in Georgia. The label should reflect a high-end, classy image and the label should suggest the chimp philanthropy without specifically naming the organization (for legal purposes). The label can be a little whimsical without being too cartoonish or child like. This wine will be sold for $30 so it should project a sense of elegance too.
Updates

holiday season makes it difficult to get feedback necessary for approval. just need a few more days...

Industry/Entity Type

Winery

Font styles to use
Sans Serif

Requirements
Must have
• Label should show common design appearance as other labels downloaded.
• Label should be a dark (emerald) green color. Label should have wine name "Albeto" in center. Label should include an image or silhouette of a chimp on it
Should not have
• no cartoonish images;

```html
<!DOCTYPE html>
<html lang="en">
<head>
<meta charset="UTF-8">
<title>Albeto Wine Label</title>
<link href="https://fonts.googleapis.com/css2?family=Sorts+Mill+Goudy&display=swap" rel="stylesheet">
<style>
  :root {
    --gold: #b38b0f;
    --green-light: #07692f;
    --green-dark: #0b4f30;
    --page: #ffffff;
  }
  html, body {
    margin: 0;
    padding: 0;
    width: 1200px;
    height: 999px;
    overflow: hidden;
    background: var(--page);
  }
  .label {
    display: block;
    width: 1200px;
    height: 999px;
  }
  .label__frame, .label__diamond-line {
    fill: none;
    stroke: var(--gold);
  }
  .label__wine-name {
    font-family: "Sorts Mill Goudy", "Goudy Old Style", serif;
    font-size: 92px;
    fill: var(--gold);
    letter-spacing: 3px;
  }
  .label__gold { fill: var(--gold); }
</style>
</head>
<body>
<svg class="label" viewBox="0 0 1200 999" xmlns="http://www.w3.org/2000/svg">
  <defs>
    <radialGradient id="emerald" cx="50%" cy="50%" r="60%">
      <stop offset="0%" stop-color="var(--green-light)"/>
      <stop offset="60%" stop-color="#086531"/>
      <stop offset="100%" stop-color="var(--green-dark)"/>
    </radialGradient>
  </defs>

  <!-- Label band -->
  <rect class="label__band" x="10" y="185" width="1180" height="628" fill="url(#emerald)"/>
  <rect class="label__frame" x="36.5" y="204.5" width="1127" height="589" stroke-width="7"/>

  <!-- Diamond emblem -->
  <polygon class="label__diamond" points="600,73 913,499 600,925 287,499" fill="url(#emerald)"/>
  <polygon class="label__diamond-line" points="600,73 913,499 600,925 287,499" stroke-width="2.5"/>
  <polygon class="label__diamond-line" points="600,100 894,499 600,898 306,499" stroke-width="5"/>
  <polygon class="label__diamond-line" points="600,112 884,499 600,886 316,499" stroke-width="2.5"/>

  <!-- Chimpanzee silhouette area -->
  <rect class="label__mascot" x="536" y="278" width="144" height="108" rx="10"
        fill="var(--gold)" role="img" aria-label="Gold silhouette of a chimpanzee walking on all fours"/>

  <!-- Upper arcs -->
  <path class="label__gold" d="M386,416 Q600,356 814,416 L808,408 Q600,352 392,408 Z"/>
  <path d="M378,428 Q600,370 822,428" fill="none" stroke="var(--gold)" stroke-width="2"/>

  <!-- Wine name -->
  <circle class="label__gold" cx="368" cy="499" r="8"/>
  <circle class="label__gold" cx="831" cy="499" r="8"/>
  <text class="label__wine-name" x="600" y="532" text-anchor="middle">ALBETO</text>

  <!-- Lower rules -->
  <rect class="label__gold" x="404" y="605" width="392" height="2.5"/>
  <polygon class="label__gold" points="410,613 790,613 784,621 416,621"/>
</svg>
</body>
</html>
```